Cloud Hosted Phone System for small and medium sized businesses

I want to design a one A4 page size single or double sided brochure to offer cloud hosted VoIP Phone system and a complete collaboration system. We have partnered with a VoIP Phone system company and want to sell their services but we don't want their name to be shown on the brochure because customers might call them directly. The company name is Our (www.kestraltechsolutions-example.com) and our company name is KESTRAL Tech Solutions. I have also uploaded my compnay's logo that you should show on the brochure. For more details about the product, you can visit their website as mentioned above.

Reason: Not getting a design to my liking.

Target Market(s)

Small and medium sized business including law firms, marketing and advertising agencies, real-estate firms and others.

Industry/Entity Type

Voip

Colors

Designer to choose colors to be used in the design.

Requirements
Must have
• My company's Logo (KESTRAL Tech Solutions). Price list, services and some images to show the benefits and services of the cloud based and advanced VoIP phone system. I want the brochure to look very professional and attractive.
• Contact US: Our company's name, Logo, web address, phone (555-371-9046) and email (info@kestraltechsolutions-example.com)
Nice to have
• It is a Canadian based company and all of our servers and customers’ data reside in Canada.

```html
<!DOCTYPE html>
<html lang="en">
<head>
<meta charset="utf-8">
<title>KESTRAL Tech Solutions – Cloud Phone System Brochure</title>
<link href="https://fonts.googleapis.com/css2?family=Raleway:wght@400;500;700;800&family=Cabin:wght@400;500&display=swap" rel="stylesheet">
<style>
:root{
  --sky-top:#4f9fd8;
  --sky-light:#dcedf9;
  --feature-blue:#1d8fd1;
  --plan-blue:#2b5d9c;
  --brand-blue:#2a5a98;
  --green:#6cbf65;
  --icon-green:#5cb865;
  --ink:#222;
  --muted:#666;
  --white:#fff;
}
*{box-sizing:border-box;margin:0;padding:0}
html,body{width:1200px;height:848px;overflow:hidden;background:#fff}
body{font-family:"Cabin",sans-serif;color:var(--ink);position:relative}
.page{position:absolute;top:0;width:600px;height:848px;overflow:hidden;border:1px solid #ccc}
.page--inside{left:0}
.page--cover{left:600px;background:#fff}

.sky{position:absolute;left:0;top:0;width:600px;height:848px;
  background:linear-gradient(180deg,var(--sky-top) 0%,#a9d2ef 12%,var(--sky-light) 22%,#fff 38%,#fff 100%)}
.section-title{position:absolute;left:45px;top:83px;font-family:"Raleway",sans-serif;font-weight:800;font-size:23px;color:#2b2b2b;letter-spacing:.2px}

.feature-box{position:absolute;top:113px;height:263px;background:var(--feature-blue);color:var(--white);padding:13px 10px 0 15px}
.feature-box--a{left:45px;width:249px}
.feature-box--b{left:308px;width:250px;padding-left:13px;padding-right:40px}
.feature-list{list-style:none;font-size:15px;line-height:18px}
.feature-list li{position:relative;padding-left:15px;margin-bottom:3.5px}
.feature-list li::before{content:"•";position:absolute;left:0;font-size:11px}

.plans{position:absolute;left:45px;top:387px;width:513px;height:183px;background:var(--plan-blue);padding:6px 15px}
.plans table{width:100%;border-collapse:separate;border-spacing:0;color:#fff;font-size:11.6px}
.plans td,.plans th{border:1.4px solid #fff;height:19.8px;padding:0 10px;font-weight:400;text-align:left}
.plans thead th{font-family:"Raleway",sans-serif;font-weight:700;font-size:11.5px;text-align:center;height:18px}
.plans thead th.plans-title{border:none;text-align:left;font-size:20.5px;font-weight:800;padding-left:12px}
.plans col.c1{width:225px}

.about{position:absolute;left:39px;top:577px;width:524px;height:153px;background:var(--green)}
.about-title{font-family:"Raleway",sans-serif;font-weight:800;font-size:18px;color:#213a2a;text-align:center;padding-top:10px}
.about-body{position:absolute;left:11px;top:36px;width:502px;height:107px;background:#fff;padding:6px 8px;font-size:11.2px;line-height:14.3px;text-align:justify}
.about-body p+p{margin-top:5px}

.brand{position:absolute;display:flex;align-items:center;font-family:"Raleway",sans-serif;font-weight:500;color:var(--brand-blue)}
.brand-mark{border-radius:50%;background:var(--brand-blue);flex:none}
.brand-name{line-height:1}
.brand--small{left:89px;top:750px}
.brand--small .brand-mark{width:44px;height:44px;margin-right:10px}
.brand--small .brand-name span{display:block}
.brand--small .n1{font-size:31px}
.brand--small .n2{font-size:15.5px;margin-top:2px}
.contact{position:absolute;left:292px;top:754px;width:272px;height:56px;background:var(--plan-blue);color:#fff;font-size:11px;line-height:15px;padding:6px 10px;white-space:nowrap}

.hero{position:absolute;left:0;top:0;width:600px;height:406px;
  background:linear-gradient(160deg,#3d8fd2 0%,#7db9e6 35%,#cfe6f7 60%,#eef6fc 80%,#fff 100%)}
.tagline{position:absolute;left:68px;top:426px;font-family:"Raleway",sans-serif;font-size:24px;font-weight:500;color:#222;transform:rotate(-9.5deg);transform-origin:left center;white-space:nowrap;letter-spacing:.3px}
.tagline b{font-weight:800;color:var(--brand-blue);font-size:27px}
.cover-band{position:absolute;left:0;top:473px;width:600px;height:34px;background:var(--brand-blue);color:#fff;font-family:"Raleway",sans-serif;font-weight:500;font-size:19px;text-align:center;line-height:34px}
.services{position:absolute;left:65px;top:543px;width:520px;display:flex}
.service{width:116px;text-align:center}
.service svg{display:block;margin:0 auto 10px}
.service h3{font-weight:400;font-size:10.2px;color:#333;line-height:12px}
.service p{font-size:6.6px;color:var(--muted);line-height:10px;margin-top:4px}
.faint-photo{position:absolute;left:330px;top:700px;width:270px;height:148px;background:radial-gradient(ellipse at 60% 55%,#e3e9ef 0%,#f3f6f8 55%,#fff 80%)}
.brand--large{left:174px;top:706px}
.brand--large .brand-mark{width:64px;height:64px;margin-right:14px}
.brand--large .n1{display:block;font-size:44px}
.brand--large .n2{display:block;font-size:21px;margin-top:2px}
</style>
</head>
<body>

<section class="page page--inside">
  <div class="sky" role="img" aria-label="Bright blue sky with soft white clouds"></div>
  <h2 class="section-title">INCLUDED FEATURES</h2>

  <div class="feature-box feature-box--a">
    <ul class="feature-list">
      <li>Access to Our Online Portal</li>
      <li>Company Greeting Message (24h/7)</li>
      <li>Company's Directory</li>
      <li>Company And User Voicemail</li>
      <li>Outbound Called Id</li>
      <li>Voicemail To Email</li>
      <li>Call Forwarding</li>
      <li>Find-me/follow-me</li>
      <li>Call Waiting</li>
      <li>Automatic Phone Relocation</li>
    </ul>
  </div>
  <div class="feature-box feature-box--b">
    <ul class="feature-list">
      <li>Remote Office Calling &amp; Transfering</li>
      <li>Phone Queueing Service</li>
      <li>Fraud Monitoring</li>
      <li>Custom Music On Hold</li>
      <li>Optional Hidden Caller Id</li>
      <li>Authorization Code Before Dialing</li>
      <li>Remote Answer</li>
      <li>Call Recording</li>
      <li>And More...</li>
    </ul>
  </div>

  <div class="plans">
    <table>
      <colgroup><col class="c1"><col><col><col></colgroup>
      <thead>
        <tr><th class="plans-title">SERVICE PLANS</th><th>BASIC</th><th>ENHANCED</th><th>PREMIUM</th></tr>
      </thead>
      <tbody>
        <tr><td>MONTHLY ACCOUNT FEE' (PER SITE)</td><td>$45,00</td><td>$45,00</td><td>$45,00</td></tr>
        <tr><td>MONTHLY USER FEE STARTING AT:</td><td></td><td></td><td></td></tr>
        <tr><td>0 TO 19 USERS</td><td>$18,00</td><td>$ 20,00</td><td>$ 22,00</td></tr>
        <tr><td>20 TO 49 USERS</td><td>$15,00</td><td>$ 17,00</td><td>$ 19,00</td></tr>
        <tr><td>50 TO 99 USERS</td><td>$12,00</td><td>$ 14,00</td><td>$ 16,00</td></tr>
        <tr><td>100 TO 199 USERS</td><td>$10,00</td><td>$ 12,00</td><td>$ 14,00</td></tr>
        <tr><td>200+ USERS</td><td>$8,00</td><td>$ 10,00</td><td>$ 12,00</td></tr>
      </tbody>
    </table>
  </div>

  <div class="about">
    <h2 class="about-title">A CLOUD-BASED PHONE SYSTEM FOR BUSINESSES</h2>
    <div class="about-body">
      <p>We can help you grow your business by modernizing your company's phone system and making it easy to use, manage, and track directly from the cloud</p>
      <p>Our cloud business phone system adapts to your economic challenges and brings flexibility and adaptability to your business communications whilst considerably reducing costs compared to traditional phone systems. We take great pride in continually improving our platform as well as developing new features and services that in turn increase our customers' productivity.</p>
    </div>
  </div>

  <div class="brand brand--small">
    <span class="brand-mark"></span>
    <span class="brand-name"><span class="n1">KESTRAL</span><span class="n2">Tech Solutions</span></span>
  </div>
  <div class="contact">
    Web : www.kestraltechsolutions-example.com<br>
    Phone : 555-371-9046<br>
    Email : info@kestraltechsolutions-example.com
  </div>
</section>

<section class="page page--cover">
  <div class="hero" role="img" aria-label="Desk IP phone in front of blue cloud shapes and sweeping blue ribbons"></div>
  <p class="tagline">YOUR SOURCE FOR ALL <b>IT SOLUTIONS</b></p>
  <h1 class="cover-band">A CLOUD-BASED PHONE SYSTEM FOR BUSINESSES</h1>

  <div class="services">
    <div class="service">
      <svg width="70" height="60" viewBox="0 0 70 60" fill="none" stroke="var(--icon-green)" stroke-width="1.6">
        <path d="M38 18a8 8 0 0 1 15-4 7 7 0 0 1 10 7 6 6 0 0 1-2 12H52"/>
        <rect x="8" y="22" width="10" height="28" rx="3" fill="var(--icon-green)"/>
        <rect x="20" y="26" width="26" height="26" rx="3" fill="var(--icon-green)"/>
        <rect x="25" y="30" width="16" height="6" fill="#fff" stroke="none"/>
        <g fill="#fff" stroke="none"><circle cx="27" cy="41" r="1.4"/><circle cx="33" cy="41" r="1.4"/><circle cx="39" cy="41" r="1.4"/><circle cx="27" cy="46" r="1.4"/><circle cx="33" cy="46" r="1.4"/><circle cx="39" cy="46" r="1.4"/></g>
      </svg>
      <h3>Cloud Phone System</h3>
      <p>Your business phone system, now in the cloud. Access every feature from anywhere.</p>
    </div>
    <div class="service">
      <svg width="70" height="60" viewBox="0 0 70 60" fill="none" stroke="var(--icon-green)" stroke-width="1.3">
        <text x="29" y="7" font-size="6" fill="var(--icon-green)" stroke="none" font-family="Cabin, sans-serif">SMS</text>
        <g stroke-dasharray="2 2"><path d="M35 30L20 18M35 30L50 18M35 30L20 44M35 30L50 44M35 30V52"/></g>
        <circle cx="18" cy="14" r="3"/><path d="M13 22a5 5 0 0 1 10 0"/>
        <path d="M47 18a4 4 0 0 1 7-2 3 3 0 0 1 2 5h-9z"/>
        <rect x="14" y="41" width="10" height="7"/><rect x="46" y="41" width="10" height="7"/>
        <rect x="30" y="51" width="10" height="7"/><path d="M30 51l5 4 5-4"/>
      </svg>
      <h3>Unified<br>Communications</h3>
      <p>A powerful suite of communications and collaboration tools grouped under one platform.</p>
    </div>
    <div class="service">
      <svg width="70" height="60" viewBox="0 0 70 60" fill="none" stroke="var(--icon-green)" stroke-width="1.6">
        <path d="M20 30a15 15 0 0 1 30 0"/>
        <rect x="15" y="28" width="7" height="13" rx="3"/>
        <rect x="48" y="28" width="7" height="13" rx="3"/>
        <path d="M51 41c0 8-6 11-13 11"/><rect x="32" y="49" width="7" height="5" rx="2"/>
      </svg>
      <h3>Contact Center</h3>
      <p>Manage your different customer contact points from a unified, user-friendly web interface.</p>
    </div>
    <div class="service">
      <svg width="70" height="60" viewBox="0 0 70 60" fill="none" stroke="var(--icon-green)" stroke-width="1.6">
        <rect x="12" y="6" width="46" height="40" rx="2"/>
        <rect x="12" y="6" width="46" height="7" fill="var(--icon-green)"/>
        <path d="M18 20h20M18 26h26M18 32h12"/>
        <circle cx="40" cy="42" r="5" fill="#fff"/><path d="M37 46l-6 10m2-3l3 2"/>
      </svg>
      <h3>Team Studio©</h3>
      <p>A flexible yet easy-to-use online administration portal to manage your business phone system.</p>
    </div>
  </div>

  <div class="faint-photo" role="img" aria-label="Faint desk phone in soft grey tones"></div>
  <div class="brand brand--large">
    <span class="brand-mark"></span>
    <span class="brand-name"><span class="n1">KESTRAL</span><span class="n2">Tech Solutions</span></span>
  </div>
</section>

</body>
</html>
```